Detail Shop Business card design

i need a business card design for my new detailing company called 'Brenner's Detail Shop'. i want an all black and white design . simple, direct and to the point. i want the designer to choose a fitting font to match the logothe front should have logo, address, phone and email and the back side should have a slogan and text indicating that we offer services on anything including cars, trucks, motorcycles and RVs. slogan will read "we take pride in your ride"
maybe also very small on the back side the IG icon with Brenners_Detail_Shop

phone 482.615.7734
address 7384 E Harlow Ave
Spokane WA 99342
email: BrennersDetail@quorvail.com

Target Market(s)

all ages , auto enthusiasts

Industry/Entity Type

Automotive

Contact Information for Business Card

the front should have logo, address, phone and email and the back side should have a slogan and text indicating that we offer services on anything including cars, trucks, motorcycles and RVs. slogan will read "we take pride in your ride"

phone 482.615.7734
address 7384 E Harlow Ave
Spokane WA 99342

Colors
000000
ffffff

Requirements
Must have
• bold font and very simple design with good spacing
Nice to have
• anything creative from the designer indicating we service any types of vehicles
Should not have
• any colors ,

```html
<!DOCTYPE html>
<html lang="en">
<head>
<meta charset="utf-8">
<title>Brenner's Detail Shop – Business Cards</title>
<link href="https://fonts.googleapis.com/css2?family=Arimo:wght@400;700&display=swap" rel="stylesheet">
<style>
  :root {
    --ink: #000000;
    --paper: #ffffff;
    --stage: #2b2b2b;
    --swoosh: #a9a9a9;
    --muted: #444444;
  }
  * { box-sizing: border-box; margin: 0; padding: 0; }
  html, body {
    width: 1200px; height: 997px; overflow: hidden;
    background: var(--stage);
    font-family: "Arimo", Arial, sans-serif;
  }
  .stage {
    width: 1200px; height: 997px;
    display: flex; flex-direction: column;
    align-items: center; justify-content: center; gap: 60px;
  }
  .card {
    position: relative; width: 700px; height: 400px;
    background: var(--paper); overflow: hidden;
  }
  .card-shapes { position: absolute; inset: 0; }
  .wordmark {
    position: absolute; left: 0; right: 0;
    display: flex; align-items: center; justify-content: center; gap: 14px;
    color: var(--ink); font-weight: 700; text-transform: uppercase;
  }
  .wordmark-dot {
    width: 22px; height: 22px; border-radius: 50%; background: var(--ink);
  }

  /* back */
  .back .slogan {
    position: absolute; top: 58px; width: 100%; text-align: center;
    font-size: 15px; letter-spacing: 4px; color: var(--muted); text-transform: uppercase;
  }
  .back .wordmark { top: 110px; font-size: 30px; letter-spacing: 1px; }
  .back .services {
    position: absolute; top: 178px; width: 100%; text-align: center;
    font-size: 14px; line-height: 1.6; letter-spacing: 1.5px; color: var(--muted);
    text-transform: uppercase;
  }
  .back .handle {
    position: absolute; left: 36px; bottom: 36px;
    display: flex; align-items: center; gap: 12px;
    color: var(--paper); font-size: 17px; letter-spacing: 1.5px; text-transform: uppercase;
  }
  .handle-icon {
    width: 28px; height: 28px; border-radius: 50%; background: var(--paper);
  }

  /* front */
  .front .wordmark { top: 120px; font-size: 36px; letter-spacing: 1px; }
  .front .contact {
    position: absolute; left: 40px; top: 262px;
    list-style: none; font-size: 18px; color: var(--ink);
  }
  .front .contact li { display: flex; align-items: center; gap: 14px; margin-bottom: 10px; }
  .contact-icon { width: 20px; height: 20px; }
  .front .address {
    position: absolute; right: 34px; top: 190px; text-align: right;
    color: var(--paper); font-size: 17px; line-height: 1.4;
  }
  .front .address svg { display: block; margin: 0 0 8px auto; }
</style>
</head>
<body>
<main class="stage">

  <section class="card back" aria-label="Card back">
    <svg class="card-shapes" viewBox="0 0 700 400" aria-hidden="true">
      <path d="M0,232 Q300,300 700,330 L700,352 Q300,326 0,258 Z" fill="var(--swoosh)"/>
      <path d="M0,258 Q300,326 700,352 L700,400 L0,400 Z" fill="var(--ink)"/>
    </svg>
    <p class="slogan">We take pride in your ride</p>
    <div class="wordmark"><span class="wordmark-dot"></span><span>Brenner's Detail Shop</span></div>
    <p class="services">We offer services on anything including<br>cars, trucks, motorcycles and RVs</p>
    <div class="handle"><span class="handle-icon"></span><span>Brenners_Detail_Shop</span></div>
  </section>

  <section class="card front" aria-label="Card front">
    <svg class="card-shapes" viewBox="0 0 700 400" aria-hidden="true">
      <path d="M0,352 Q420,335 700,112 L700,140 Q420,362 0,378 Z" fill="var(--swoosh)"/>
      <path d="M0,378 Q420,362 700,140 L700,400 L0,400 Z" fill="var(--ink)"/>
    </svg>
    <div class="wordmark"><span class="wordmark-dot"></span><span>Brenner's Detail Shop</span></div>
    <ul class="contact">
      <li>
        <svg class="contact-icon" viewBox="0 0 20 20" aria-hidden="true">
          <circle cx="10" cy="10" r="10" fill="var(--ink)"/>
          <path d="M6.5,5 l2,0 l1,2.5 l-1.3,1 q1,2 3,3 l1,-1.3 l2.5,1 l0,2 q-5,0.5 -8.2,-4.2 q-1.2,-2 -1,-4 z" fill="var(--paper)"/>
        </svg>
        <span>482.615.7734</span>
      </li>
      <li>
        <svg class="contact-icon" viewBox="0 0 20 20" aria-hidden="true">
          <circle cx="10" cy="10" r="10" fill="var(--ink)"/>
          <rect x="5" y="6.5" width="10" height="7" fill="var(--paper)"/>
          <path d="M5,6.5 L10,10.5 L15,6.5" fill="none" stroke="var(--ink)" stroke-width="1"/>
        </svg>
        <span>BrennersDetail@quorvail.com</span>
      </li>
    </ul>
    <address class="address">
      <svg width="20" height="20" viewBox="0 0 20 20" aria-hidden="true">
        <circle cx="10" cy="10" r="10" fill="var(--paper)"/>
        <path d="M10,4 a4,4 0 0 1 4,4 c0,3 -4,8 -4,8 c0,0 -4,-5 -4,-8 a4,4 0 0 1 4,-4 z" fill="var(--ink)"/>
        <circle cx="10" cy="8" r="1.5" fill="var(--paper)"/>
      </svg>
      7384 E Harlow Ave<br>Spokane WA 99342
    </address>
  </section>

</main>
</body>
</html>
```